We need a nice multi-page site that is new cutting edge and reflect who we are in Miami Beach and the world.

We have an existing site and we need to make the new one more user friendly, video uploads, word press base, nice soft touch with our logo, sexy look

Present site www.brenvitalis-example.com

Target Market(s)

Upscale high end demographic traveling to and from Miami Beach

Industry/Entity Type

Clinic

Requirements
Must have
• 1) Very Refined elegant site, clean ...Corvalinesq...www.corvaline-example.com...www.marquetto-example.com..Logo in middle of page, nice placed and drop-down toward the sides
2) Very visual and inviting
3) We need to tell the story of our health care model, Dr Stefan Orwick traveling around the world bringing back to BVC, a unique holistic health care model based on three main points....we can get into that later
4) Contact us call to action button
5) Newsletter option
6) E-commerce section
Should not have
• Not too cheeky, not canned, button and boxes off the shelf

```html
<!DOCTYPE html>
<html lang="en">
<head>
<meta charset="utf-8">
<title>Brenwick Vitality Clinic</title>
<link rel="stylesheet" href="https://fonts.googleapis.com/css2?family=Open+Sans:wght@400;600;700&family=Arimo:wght@400;700&display=swap">
<style>
:root{
  --sky-deep:#63c8f4;
  --sky-mid:#8fd7f7;
  --sky-pale:#eaf8fe;
  --ink:#3d3d3d;
  --ink-soft:#555b60;
  --heading-blue:#3f86c4;
  --link-blue:#1f86d6;
  --red:#e0262a;
  --red-dark:#b81a1e;
  --white:#ffffff;
  --panel:rgba(255,255,255,.42);
}
*{box-sizing:border-box;margin:0;padding:0}
html,body{width:1200px;height:966px;overflow:hidden}
body{position:relative;font-family:"Arimo",Arial,sans-serif;color:var(--ink);background:var(--white)}
.header{position:absolute;left:0;top:0;width:1200px;height:159px;
  background:radial-gradient(ellipse 420px 170px at 590px 60px,var(--white) 0%,var(--sky-pale) 35%,#b8e6fb 70%,var(--sky-mid) 100%)}
.brand{position:absolute;left:470px;top:62px;width:290px;text-align:center;
  font-family:"Open Sans",sans-serif;font-weight:400;font-size:19px;letter-spacing:.5px;color:#4a4a4a;white-space:nowrap}
.brand-dot{position:absolute;left:556px;top:86px;width:12px;height:12px;border-radius:50%;background:#6aa3cf}
.phone{position:absolute;left:796px;top:24px;display:flex;align-items:center;gap:6px;font-size:14px;color:#333}
.free{position:absolute;left:840px;top:45px;width:86px;text-align:right;font-size:8px;font-style:italic;color:#3f7fb8}
.search{position:absolute;left:810px;top:77px;display:flex}
.search-field{width:76px;height:20px;border:1px solid #9ccbe4;border-radius:4px 0 0 4px;background:linear-gradient(#fff,#eef8fd)}
.search-btn{width:40px;height:20px;background:var(--red);color:#fff;font-size:9px;line-height:20px;text-align:center;border-radius:0 3px 3px 0}
.nav{position:absolute;left:0;top:159px;width:1200px;height:26px;background:var(--white);border-bottom:1px solid #cde6f2;
  box-shadow:0 1px 3px rgba(0,0,0,.12)}
.nav ul{list-style:none;position:absolute;left:345px;top:6px;display:flex;font-size:11px;color:#444}
.nav li{margin-right:27px}
.nav li:nth-child(4){margin-right:20px}
.main{position:absolute;left:0;top:185px;width:1200px;height:673px;
  background:radial-gradient(ellipse 500px 280px at 560px 180px,#c9ecfc 0%,#9ddcf8 45%,var(--sky-deep) 100%)}
.doctor-photo{position:absolute;left:280px;top:193px;width:140px;height:190px;border-radius:60px 60px 6px 6px;
  background:linear-gradient(180deg,#c8a58d 0%,#e9eef1 38%,#ffffff 70%,#dfe7ec 100%)}
.hero-panel{position:absolute;left:415px;top:205px;width:510px;height:150px;background:var(--panel);border-radius:4px}
.hero-name{position:absolute;left:440px;top:229px;font-family:"Open Sans",sans-serif;font-weight:700;font-size:22px;color:var(--heading-blue)}
.hero-text{position:absolute;left:440px;top:255px;width:475px;font-family:"Open Sans",sans-serif;font-size:17px;line-height:21px;color:#3b3b3b}
.btn-contact{position:absolute;left:773px;top:330px;width:133px;height:41px;border-radius:3px;
  background:linear-gradient(#f0403f,var(--red-dark));color:#fff;font-size:17px;text-align:center;line-height:41px;
  font-family:"Open Sans",sans-serif;box-shadow:0 2px 3px rgba(0,0,0,.2)}
.unique-title{position:absolute;left:257px;top:407px;font-family:"Open Sans",sans-serif;font-size:22px;color:var(--heading-blue)}
.unique-body{position:absolute;left:259px;top:445px;width:374px;height:190px;overflow:hidden;font-size:8.6px;line-height:12.8px;color:var(--ink-soft)}
.unique-body p{margin-bottom:12.8px}
.read-more{position:absolute;left:573px;top:643px;font-size:8.5px;color:var(--link-blue)}
.news-title{position:absolute;left:699px;top:425px;font-size:17px;color:#333}
.news-label{position:absolute;left:702px;top:461px;font-size:12px;color:#333}
.news-field{position:absolute;left:806px;top:457px;width:120px;height:21px;background:#fff;border:1px solid #a9d6ec;border-radius:5px}
.btn-small{position:absolute;height:20px;border-radius:5px;background:linear-gradient(#f0403f,var(--red-dark));color:#fff;text-align:center;line-height:20px}
.btn-submit{left:866px;top:486px;width:60px;font-size:12px}
.btn-shop{left:850px;top:638px;width:74px;height:24px;line-height:24px;font-size:9.5px;border-radius:3px}
.treat-title{position:absolute;left:698px;top:519px;font-size:17px;color:#333}
.arrow{position:absolute;color:#eaf7fd;font-family:"Open Sans",sans-serif}
.treat{position:absolute;top:553px;width:56px;text-align:center;font-size:7px;line-height:7px;color:#333}
.treat-img{width:54px;height:53px;margin:0 auto 3px;background:#fff;padding:3px}
.treat-img div{width:100%;height:100%;border-radius:50%;background:radial-gradient(circle,#e8d8ef,#a27ab8)}
.treat-img.bottle div{border-radius:4px;background:linear-gradient(#f3ede8,#e6b9a6)}
.videos-title{position:absolute;left:261px;top:690px;font-family:"Open Sans",sans-serif;font-size:17px;color:var(--heading-blue)}
.video{position:absolute;top:727px;width:135px;text-align:center;font-size:9px;color:#333}
.video-frame{width:135px;height:87px;background:#fff;padding:4px;border-radius:2px;margin-bottom:4px;box-shadow:0 1px 2px rgba(0,0,0,.15)}
.video-frame div{width:100%;height:100%}
.v-portrait{background:linear-gradient(90deg,#f4ece6,#f6f2ee 60%,#fdfdfd)}
.v-scrubs{background:linear-gradient(#2ab0d8,#18a0cc)}
.footer-nav{position:absolute;left:261px;top:882px;display:flex;font-size:9.5px;color:#444;list-style:none}
.footer-nav li{margin-right:16px}
.footer-nav li:nth-child(4){margin-right:12px}
.follow{position:absolute;left:841px;top:882px;font-size:11px;color:#333}
.social{position:absolute;left:841px;top:904px;display:flex;gap:3px}
.social span{width:13px;height:16px;background:#3b7fc0;border-radius:2px}
</style>
</head>
<body>
<header class="header">
  <div class="brand-dot"></div>
  <div class="brand">BRENWICK VITALITY CLINIC</div>
  <div class="phone">
    <svg width="18" height="22" viewBox="0 0 18 22"><path d="M4 1 L8 5 L6 8 C7 11 9 14 12 15 L14 13 L17 17 L14 20 C7 19 2 12 1 4 Z" fill="none" stroke="#2aa0d8" stroke-width="1.6"/></svg>
    Call 305 555 0148
  </div>
  <div class="free">Free Consultation!</div>
  <div class="search"><div class="search-field"></div><div class="search-btn">search</div></div>
</header>

<nav class="nav">
  <ul>
    <li>About Brenwick Vitality</li>
    <li>Products / Services</li>
    <li>Health Wisdom</li>
    <li>Appointments</li>
    <li>Contact Us</li>
  </ul>
</nav>

<main class="main"></main>

<div class="doctor-photo" role="img" aria-label="Portrait photo of the clinic doctor in a white coat"></div>
<div class="hero-panel"></div>
<h1 class="hero-name">Dr Stefan Orwick</h1>
<p class="hero-text">traveling around the world bringing back to BVC, a unique holistic health care model based on three main points</p>
<div class="btn-contact">CONTACT US</div>

<h2 class="unique-title">How we are Unique</h2>
<div class="unique-body">
  <p>Unparalleled service along with a constant desire to stay up to date, Brenwick Vitality Clinic is a one of a kind “hybrid” model for health and wellness, founded by an American family with a long history as healthcare providers and staffed with certified medical doctors trained in the United States. We focus on an integrative and functional medical approach to patient health concerns and understand the practice of medicine is a matter of trust. We strive ensure you know your options and have a say in your health care.</p>
  <p>Aware that bureaucratic systems and insurance companies have made medicine a very limiting practice, we work exclusively on a fee-for-service basis. To facilitate good health, offer many preventative, rejuvenative and wellness programs around enhancement of diet, lifestyle, and mindset, also screening for diseases and providing full physical exams in a private, modern, and tranquil setting.</p>
  <p>Most importantly, we truly understand health care and want to serve your individual needs. Whether in Mexico City or New York City, Los Angeles or London, our physicians can work with</p>
</div>
<div class="read-more">Read more&gt;&gt;</div>

<h2 class="news-title">Get Our Newsletter</h2>
<div class="news-label">Email:</div>
<div class="news-field"></div>
<div class="btn-small btn-submit">submit</div>

<h2 class="treat-title">Our treatments</h2>
<div class="arrow" style="left:696px;top:566px;font-size:26px">❬</div>
<div class="arrow" style="left:914px;top:566px;font-size:26px">❭</div>
<div class="treat" style="left:713px"><div class="treat-img" role="img" aria-label="Product photo of a lavender cream jar"><div></div></div>Honeydrop herbal tonic</div>
<div class="treat" style="left:785px;top:550px"><div class="treat-img bottle" role="img" aria-label="Product photo of a skincare bottle and powder"><div></div></div>Honeydrop herbal tonic</div>
<div class="treat" style="left:856px;top:555px"><div class="treat-img" role="img" aria-label="Product photo of a lavender cream jar"><div></div></div>Honeydrop herbal tonic</div>
<div class="btn-small btn-shop">visit our shop</div>

<h2 class="videos-title">Videos Upload</h2>
<div class="arrow" style="left:256px;top:740px;font-size:38px">❬</div>
<div class="arrow" style="left:910px;top:740px;font-size:38px">❭</div>
<div class="video" style="left:284px"><div class="video-frame"><div class="v-portrait" role="img" aria-label="Video still of a smiling nurse"></div></div>Honeydrop herbal tonic</div>
<div class="video" style="left:447px"><div class="video-frame"><div class="v-scrubs" role="img" aria-label="Video still of a doctor in scrubs holding a clipboard"></div></div>Honeydrop herbal tonic</div>
<div class="video" style="left:609px"><div class="video-frame"><div class="v-scrubs" role="img" aria-label="Video still of a doctor in scrubs with arms crossed"></div></div>Honeydrop herbal tonic</div>
<div class="video" style="left:771px"><div class="video-frame"><div class="v-portrait" role="img" aria-label="Video still of a smiling nurse"></div></div>Honeydrop herbal tonic</div>

<footer>
  <ul class="footer-nav">
    <li>About Brenwick Vitality</li>
    <li>Products / Services</li>
    <li>Health Wisdom</li>
    <li>Appointments</li>
    <li>Contact Us</li>
  </ul>
  <div class="follow">Follow us</div>
  <div class="social" aria-label="Social links"><span></span><span></span><span></span><span></span><span></span></div>
</footer>
</body>
</html>
```